Webdesign für Projektmanagement
Zielgruppe
Projektmanagement und Projektsteuerung von Bauvorhaben für Projektentwickler und Bauträger.
Wesentliche Bereiche sind Wirtschaftliche Steuerung, Steuerung der Baustelle und Bauabläufe sowie Steuerung der Marketing und Vertriebsaktivitäten.
Aufgabenstellung
Orientierung am Logo. Logo und Visitenkarte liegen bei. Schriftart Prelo und Prelo Slab.

```html
<!DOCTYPE html>
<html lang="de">
<head>
<meta charset="utf-8">
<title>Hallberg Real Estate</title>
<link href="https://fonts.googleapis.com/css2?family=Roboto+Condensed:wght@300;400;700&family=Roboto:wght@400&display=swap" rel="stylesheet">
<style>
  :root {
    --navy: #021420;
    --navy-header: #03131f;
    --gold: #a08c4a;
    --white: #ffffff;
    --cream: #f4f1ea;
    --footer-bg: #ffffff;
    --footer-text: #1a1f26;
  }
  * { margin: 0; padding: 0; box-sizing: border-box; }
  html, body { width: 1200px; height: 1200px; overflow: hidden; background: var(--navy); }
  body { position: relative; font-family: "Roboto Condensed", sans-serif; color: var(--white); }

  .site-header { position: absolute; left: 0; top: 0; width: 1200px; height: 90px; background: var(--navy-header); }
  .brand { position: absolute; left: 149px; top: 30px; font-family: "Roboto Condensed", sans-serif; font-weight: 700; font-size: 26px; line-height: 30px; color: var(--gold); letter-spacing: 0.3px; }
  .main-nav { position: absolute; top: 0; left: 0; }
  .main-nav a { position: absolute; top: 61px; font-size: 13px; line-height: 16px; color: var(--white); text-decoration: none; letter-spacing: 0.2px; white-space: nowrap; }
  .main-nav a.is-active::after { content: ""; position: absolute; left: -3px; right: -3px; top: 26px; height: 2px; background: var(--gold); }

  .hero { position: absolute; left: 0; top: 90px; width: 1200px; height: 535px;
    background: linear-gradient(180deg, #1c2a3a 0%, #3a3a36 35%, #6b5a3a 58%, #3c3a34 75%, #2a2f34 100%); }
  .hero-shade { position: absolute; inset: 0; background: rgba(8, 16, 26, 0.35); }
  .hero-title { position: absolute; left: 0; width: 1200px; text-align: center; color: var(--cream); font-weight: 400; text-shadow: 0 2px 6px rgba(0,0,0,0.4); }
  .hero-title .line-small { position: absolute; left: 0; width: 1200px; top: 150px; font-size: 56px; line-height: 64px; letter-spacing: 1px; }
  .hero-title .line-large { position: absolute; left: 0; width: 1200px; top: 198px; font-size: 96px; line-height: 110px; letter-spacing: 3px; }
  .scroll-down { position: absolute; left: 576px; top: 434px; width: 48px; height: 48px; }

  .about { position: absolute; left: 0; top: 625px; width: 1200px; height: 521px; background: var(--navy); }
  .about-title { position: absolute; top: 82px; left: 0; width: 1200px; text-align: center; font-weight: 300; font-size: 40px; line-height: 48px; letter-spacing: 0.5px; }
  .about-title strong { font-weight: 700; }
  .service { position: absolute; top: 175px; width: 300px; text-align: center; }
  .service-icon { display: block; margin: 0 auto; width: 52px; height: 52px; }
  .service-name { margin-top: 38px; font-size: 21px; line-height: 26px; font-weight: 400; color: var(--gold); letter-spacing: 0.3px; }
  .service-text { margin-top: 6px; font-family: "Roboto", sans-serif; font-size: 11.5px; line-height: 16.5px; color: var(--white); }
  .service-button { display: block; margin: 40px auto 0; width: 150px; height: 33px; border: 1px solid var(--gold); color: var(--gold); font-size: 11px; line-height: 31px; text-decoration: none; }

  .site-footer { position: absolute; left: 0; top: 1146px; width: 1200px; height: 54px; background: var(--footer-bg); color: var(--footer-text); font-size: 9.5px; }
  .copyright { position: absolute; left: 149px; top: 21px; }
  .footer-nav a { position: absolute; top: 21px; color: var(--footer-text); text-decoration: none; }
</style>
</head>
<body>
  <header class="site-header">
    <div class="brand">Hallberg Real Estate</div>
    <nav class="main-nav">
      <a class="is-active" href="#" style="left:678px">START</a>
      <a href="#" style="left:736px">LEISTUNGEN</a>
      <a href="#" style="left:827px">ÜBER UNS</a>
      <a href="#" style="left:904px">REFERENZEN</a>
      <a href="#" style="left:997px">KONTAKT</a>
    </nav>
  </header>

  <section class="hero" role="img" aria-label="Nachtansicht eines Hafens mit moderner Architektur und Booten im Wasser">
    <div class="hero-shade"></div>
    <h1 class="hero-title">
      <span class="line-small">WIR GESTALTEN</span>
      <span class="line-large">LEBENSRAUM</span>
    </h1>
    <svg class="scroll-down" viewBox="0 0 48 48" aria-hidden="true">
      <circle cx="24" cy="24" r="23" fill="rgba(2,20,32,0.25)" stroke="var(--gold)" stroke-width="1.5"/>
      <polyline points="17,21 24,28 31,21" fill="none" stroke="var(--gold)" stroke-width="1.5"/>
    </svg>
  </section>

  <section class="about">
    <h2 class="about-title">ÜBER <strong>HALLBERG</strong> REAL ESTATE</h2>

    <article class="service" style="left:150px">
      <svg class="service-icon" viewBox="0 0 52 52" fill="none" stroke="#fff" stroke-width="1.2" aria-hidden="true">
        <rect x="2" y="10" width="48" height="36" rx="2"/>
        <path d="M19 10 V5 H33 V10"/>
        <path d="M2 22 H23 M29 22 H50"/>
        <rect x="23" y="20" width="6" height="5"/>
      </svg>
      <h3 class="service-name">PROJEKTMANAGEMENT</h3>
      <p class="service-text">Lorem ipsum dolor sit amet, consetetur sadipscing elitr,<br>sed diam nonumy eirmod tempor invidunt ut labore et<br>dolore magna aliquyam erat, sed diam voluptua.</p>
      <a class="service-button" href="#">MEHR ERFAHREN</a>
    </article>

    <article class="service" style="left:450px">
      <svg class="service-icon" viewBox="0 0 52 52" fill="none" stroke="#fff" stroke-width="1.2" aria-hidden="true">
        <rect x="6" y="2" width="34" height="46" rx="1"/>
        <path d="M11 10 H34 M11 17 H30 M11 24 H26"/>
        <path d="M33 50 V32 a3 3 0 0 1 6 0 V40 l7 2 V50"/>
      </svg>
      <h3 class="service-name">PROJEKTSTEUERUNG</h3>
      <p class="service-text">Lorem ipsum dolor sit amet, consetetur sadipscing elitr,<br>sed diam nonumy eirmod tempor invidunt ut labore et<br>dolore magna aliquyam erat, sed diam voluptua.</p>
      <a class="service-button" href="#">MEHR ERFAHREN</a>
    </article>

    <article class="service" style="left:750px">
      <svg class="service-icon" viewBox="0 0 52 52" fill="none" stroke="#fff" stroke-width="1.2" aria-hidden="true">
        <rect x="2" y="20" width="6" height="12"/>
        <path d="M8 21 L46 9 V43 L8 31"/>
        <path d="M17 34 L19 42 H27 L26 37"/>
        <path d="M46 7 V45"/>
      </svg>
      <h3 class="service-name">MARKETING &amp; VERTRIEB</h3>
      <p class="service-text">Lorem ipsum dolor sit amet, consetetur sadipscing elitr,<br>sed diam nonumy eirmod tempor invidunt ut labore et<br>dolore magna aliquyam erat, sed diam voluptua.</p>
      <a class="service-button" href="#">MEHR ERFAHREN</a>
    </article>
  </section>

  <footer class="site-footer">
    <span class="copyright">© 2017 HALLBERG REAL ESTATE GMBH</span>
    <nav class="footer-nav">
      <a href="#" style="left:879px">PARTNER</a>
      <a href="#" style="left:938px">KONTAKT</a>
      <a href="#" style="left:998px">IMPRESSUM</a>
    </nav>
  </footer>
</body>
</html>
```